Redesign of a facility management homepage

We need a redesign/an improved design of the facility management homepage (http://www.kolvenhaus-drefling.de/).
This websites offers detailed information on the "About us" as company, the "Services" provided and special information on facility and strata management. We would like to keep the structure of the website.
We need ideas/designs how this website could look more modern and confidential and appealing/pleasant for visitors at the same time and not losing the main purpose of information distribution.
The green color must be used since this is the basic color from our logo.
The blue in the background of the logo ist optional. So feel to use it or not.
We need no coding only design (.psd or as .ai)
Industry/Entity Type
It Company
Look and feel
Each slider illustrates characteristics of the customer's brand and the style your logo design should communicate.

```html
<!DOCTYPE html>
<html lang="en">
<head>
<meta charset="utf-8">
<title>KHD Office and janitorial service GmbH Drefling</title>
<link href="https://fonts.googleapis.com/css2?family=Ubuntu:wght@300;400;500&family=Open+Sans:wght@400;600&display=swap" rel="stylesheet">
<style>
:root{
  --green:#268d2f;
  --green-dark:#1f7a27;
  --text:#555;
  --link:#2a5fb5;
  --footer:#4a4748;
  --page:#f6f6f6;
  --white:#fff;
}
*{margin:0;padding:0;box-sizing:border-box}
html,body{width:890px;height:1200px;overflow:hidden}
body{position:relative;background:var(--page);font-family:"Open Sans",sans-serif;color:var(--text)}
.abs{position:absolute}
.topbar{left:0;top:0;width:890px;height:32px;background:var(--green);color:#e8f4e8;font-size:10px}
.topbar .links{left:74px;top:10px}
.topbar .contact{right:74px;top:8px;font-family:"Ubuntu",sans-serif;font-size:12px;color:#fff;display:flex;gap:8px;align-items:center}
.brand{left:74px;top:52px;width:102px;height:84px;display:flex;align-items:center;gap:6px}
.brand-mark{width:22px;height:22px;border-radius:50%;background:var(--green)}
.brand-name{font-family:"Ubuntu",sans-serif;font-size:26px;font-weight:500;color:var(--green)}
.tagline{left:188px;top:73px;font-family:"Ubuntu",sans-serif;font-size:14.5px;line-height:22px;color:var(--green)}
.search{left:663px;top:79px;width:154px;height:29px;border:1px solid #ccc;background:#fff;font-size:9px;color:#999;padding:8px 5px}
.search svg{position:absolute;right:6px;top:8px}
.nav{left:74px;top:156px;width:742px;height:42px;background:var(--green);border-radius:5px;display:flex;font-family:"Ubuntu",sans-serif;font-size:11.5px;color:#fff}
.nav a{display:flex;align-items:center;justify-content:center;border-right:1px solid #1c6e24;color:#fff;text-decoration:none}
.nav a:last-child{border:none}
.slider{left:75px;top:211px;width:740px;height:280px;background:#2c2c2c}
.slider-photo{left:0;top:0;width:511px;height:280px;background:linear-gradient(180deg,#c79a4e 0%,#d9c9a4 35%,#e6e6e6 55%,#6d6a66 100%)}
.slider-info{right:16px;top:22px;text-align:right;font-size:10.5px;line-height:25.3px;color:#fff}
.arrows{right:30px;top:242px;display:flex;gap:6px}
.arrows span{width:22px;height:22px;border-radius:50%;background:#fff;display:flex;align-items:center;justify-content:center}
.main{left:74px;top:513px;width:743px;height:603px;background:#fff;border:1px solid #ddd;z-index:2}
.welcome{left:10px;top:16px;font-family:"Ubuntu",sans-serif;font-weight:300;font-size:24px;color:var(--green)}
.intro{left:12px;top:57px;width:440px;font-size:9.6px;line-height:16.2px}
.intro p{margin-bottom:3px}
.van{left:458px;top:38px;width:265px;height:150px;background:radial-gradient(ellipse at 50% 50%,#e8eaec 0%,#d3d6d9 55%,#fff 75%)}
.divider{left:14px;top:218px;width:702px;border-top:2px dotted #ccc}
.card{top:246px;width:167px;height:197px;border:1px solid #ddd}
.card-photo{left:0;top:0;width:165px;height:160px}
.card-label{left:0;bottom:0;width:165px;height:36px;background:var(--green);color:#fff;font-family:"Ubuntu",sans-serif;font-size:13px;display:flex;align-items:center;justify-content:center;padding-top:6px}
.card-icon{left:63px;top:132px;width:40px;height:40px;border-radius:50%;background:var(--green);display:flex;align-items:center;justify-content:center}
.news-title{left:11px;top:474px;font-family:"Ubuntu",sans-serif;font-weight:400;font-size:18px;color:var(--green)}
.dots{left:442px;top:480px;display:flex;gap:3px}
.dots span{width:8px;height:8px;border-radius:50%;border:1px solid #555}
.dots span.on{background:var(--green);border-color:var(--green)}
.news-item{top:504px;width:235px;height:64px}
.news-thumb{left:0;top:0;width:87px;height:64px}
.news-item h4{position:absolute;left:97px;top:4px;font-weight:400;font-size:9px;color:var(--link);white-space:nowrap}
.news-item p{position:absolute;left:97px;top:20px;font-size:9px;line-height:13.5px;color:#444;white-space:nowrap}
.qc-title{left:496px;top:474px;font-family:"Ubuntu",sans-serif;font-weight:400;font-size:18px;color:var(--green)}
.qc-text{left:498px;top:505px;width:215px;font-size:9px;line-height:15px;color:#777}
.qc-btn{left:498px;top:543px;width:116px;height:28px;background:var(--green);color:#fff;font-size:10px;display:flex;align-items:center;justify-content:center}
.footer{left:0;top:1072px;width:890px;height:128px;background:var(--footer);color:#ddd;z-index:1}
.footer-links{left:74px;top:64px;font-size:9.8px}
.copyright{left:74px;top:87px;font-size:8.5px;color:#ccc}
.connect{left:688px;top:80px;font-family:"Ubuntu",sans-serif;font-size:11.5px;color:#fff}
.social{top:74px;width:26px;height:26px;border-radius:50%}
</style>
</head>
<body>
<div class="abs topbar">
  <div class="abs links">Support &nbsp;|&nbsp; Links &nbsp;|&nbsp; Imprint &nbsp;|&nbsp; Contact Us</div>
  <div class="abs contact">
    <svg width="12" height="12" viewBox="0 0 12 12"><rect width="12" height="12" rx="2" fill="#fff"/><path d="M3 3c0 4 2 6 6 6l1-1.5-2-1-1 1c-1-.5-2-1.5-2.5-2.5l1-1-1-2z" fill="#268d2f"/></svg>
    <span>Tel: 0 41 53/72 40 18</span><span>|</span>
    <svg width="14" height="10" viewBox="0 0 14 10"><rect width="14" height="10" fill="#fff"/><path d="M0 0l7 5 7-5" stroke="#268d2f" fill="none"/></svg>
    <span>Email: info@kolvenhaus-drefling.de</span>
  </div>
</div>

<div class="abs brand"><span class="brand-mark"></span><span class="brand-name">KHD</span></div>
<div class="abs tagline">Office and janitorial service GmbH Drefling<br>Your local partner.</div>
<div class="abs search">Search
  <svg width="11" height="11" viewBox="0 0 11 11"><circle cx="4.5" cy="4.5" r="3.5" stroke="#3a6fb5" stroke-width="1.5" fill="none"/><path d="M7 7l3 3" stroke="#3a6fb5" stroke-width="1.5"/></svg>
</div>

<nav class="abs nav">
  <a style="width:110px">Home</a>
  <a style="width:118px">About us</a>
  <a style="width:194px">Building Management</a>
  <a style="width:180px">Building management</a>
  <a style="width:140px">Rental</a>
</nav>

<div class="abs slider">
  <div class="abs slider-photo" role="img" aria-label="Row of white company vans parked in front of an office building"></div>
  <div class="abs slider-info">
    KHD office and janitorial Service GmbH<br>
    20-23 market in 07431 Drefling<br>
    represented by Ms. Mareike Tannfeld, CEO<br>
    AG Lindenau, HR.Nr.: HRB 40517<br>
    Tel: 0 41 53/72 40 18<br>
    Fax: 0 41 53/72 40 19<br>
    Email: info@kolvenhaus-drefling.de<br>
    Contact
  </div>
  <div class="abs arrows">
    <span><svg width="8" height="10" viewBox="0 0 8 10"><path d="M6 1L2 5l4 4" stroke="#333" stroke-width="2" fill="none"/></svg></span>
    <span><svg width="8" height="10" viewBox="0 0 8 10"><path d="M2 1l4 4-4 4" stroke="#333" stroke-width="2" fill="none"/></svg></span>
  </div>
</div>

<main class="abs main">
  <h1 class="abs welcome">Welcome to Our Website !!</h1>
  <div class="abs intro">
    <p>The KHD is an established, experienced and successful services company with the divisions Buildings Management (facilities management, operating expense reports, etc.), concierge service, winter maintenance, building services, secretarial services, etc.</p>
    <p>The KHD has the latest computer programs and trained, highly experienced and motivated staff.</p>
    <p>The KHD guarantees comprehensive support, thereby ensuring preservation of value of the contract objects. Furthermore, the standing KHD also for the optimization of the net results of the individual property investments in terms of costs and revenues. Most of the KHD managed objects have extremely low vacancy rates.</p>
  </div>
  <div class="abs van" role="img" aria-label="White company van with roof rack"></div>
  <div class="abs divider"></div>

  <div class="abs card" style="left:10px">
    <div class="abs card-photo" role="img" aria-label="Support agent wearing a headset" style="background:linear-gradient(160deg,#7a6a5e,#d9c3b3 60%,#f0ebe8)"></div>
    <div class="abs card-label">Report disorder online</div>
    <div class="abs card-icon"><svg width="20" height="20" viewBox="0 0 20 20"><path d="M4 11a6 6 0 0112 0" stroke="#fff" stroke-width="2" fill="none"/><rect x="2" y="10" width="4" height="6" rx="1" fill="#fff"/><rect x="14" y="10" width="4" height="6" rx="1" fill="#fff"/></svg></div>
  </div>
  <div class="abs card" style="left:195px">
    <div class="abs card-photo" role="img" aria-label="Hand holding a contact us note" style="background:linear-gradient(160deg,#f3f1ee,#e9dcc6 50%,#d8b89e)"></div>
    <div class="abs card-label">Contact</div>
    <div class="abs card-icon"><svg width="20" height="18" viewBox="0 0 20 18"><path d="M2 6c4-4 12-4 16 0l-1 3-3-1V6H6v2L3 9z" fill="#fff"/><rect x="5" y="10" width="10" height="6" rx="1" fill="#fff"/></svg></div>
  </div>
  <div class="abs card" style="left:380px">
    <div class="abs card-photo" role="img" aria-label="Hands typing on a keyboard" style="background:linear-gradient(160deg,#bfc3c6,#6e7276 55%,#3d3f42)"></div>
    <div class="abs card-label">Left</div>
    <div class="abs card-icon"><svg width="16" height="18" viewBox="0 0 16 18"><rect x="2" y="1" width="12" height="16" fill="#fff"/><path d="M4 6h8M4 9h8M4 12h8" stroke="#268d2f"/></svg></div>
  </div>
  <div class="abs card" style="left:564px">
    <div class="abs card-photo" role="img" aria-label="Cupped hands protecting a small house" style="background:linear-gradient(160deg,#c9c4c0,#d2a493 55%,#e0d6cf)"></div>
    <div class="abs card-label">Imprint</div>
    <div class="abs card-icon"><svg width="20" height="18" viewBox="0 0 20 18"><path d="M10 1L1 9h3v8h4v-5h4v5h4V9h3z" fill="#fff"/></svg></div>
  </div>

  <h2 class="abs news-title">Latest News</h2>
  <div class="abs dots"><span class="on"></span><span></span><span></span></div>
  <div class="abs news-item" style="left:11px">
    <div class="abs news-thumb" role="img" aria-label="Small blue utility vehicle" style="background:linear-gradient(160deg,#6b7a8c,#2f4f96 55%,#555)"></div>
    <h4>Lorem ipsum dolor sit amet</h4>
    <p>Lorem ipsum dolor sit amet,<br>consetetur sadipscing elitr, sed<br>diam nonumy eirmod tempor</p>
  </div>
  <div class="abs news-item" style="left:255px">
    <div class="abs news-thumb" role="img" aria-label="Rear of a white company van" style="background:linear-gradient(160deg,#444,#e8e8e8 50%,#bbb)"></div>
    <h4>Lorem ipsum dolor sit amet</h4>
    <p>Lorem ipsum dolor sit amet,<br>consetetur sadipscing elitr, sed<br>diam nonumy eirmod tempor</p>
  </div>
  <h2 class="abs qc-title">Quick Contact</h2>
  <p class="abs qc-text">Nunc tempus felis vitae urna Vivamus porttitor g purus nisi eleifend libero a tempus libero lectus</p>
  <div class="abs qc-btn">CLICK HERE</div>
</main>

<footer class="abs footer">
  <div class="abs footer-links">HOME &nbsp;|&nbsp; OUR SERVICES &nbsp;|&nbsp; BUILDING MANAGEMENT &nbsp;|&nbsp; RENTAL &nbsp;|&nbsp; CONTACT US</div>
  <div class="abs copyright">© 2014 KHD. &nbsp;All right reserved Term of Use</div>
  <div class="abs connect">Connect Us:</div>
  <div class="abs social" style="left:757px;background:#3b5a98"></div>
  <div class="abs social" style="left:790px;background:#3cc0e8"></div>
</footer>
</body>
</html>
```